ROLL UP CREATION

For a trade show we need three visuals to be seen see pdf file with slogans and photos. I expect from you a nice and attractive formatting that is urgent. the files must be in high definition for the printer. You will find enclosed the 3 visuals, photos the basic logo by adding the .com and the photo of the Rollup For a trade show we need to see the pdf file with slogans and photos. I expect from you a nice and attractive formatting that is urgent. the files must be in high definition for the printer. For a trade show we need to see the pdf file with slogans and photos. I expect from you a nice and attractive formatting that is urgent. the files must be in high definition for the printer. For a trade show we need to see the pdf file with slogans and photos. I expect from you a nice and attractive formatting that is urgent. the files must be in high definition for the printer. For a trade show we need to see the pdf file with slogans and photos. I expect from you a nice and attractive formatting that is urgent. the files must be in high definition for the printer. For a trade show we need to see the pdf file with slogans and photos. I expect from you a nice and attractive formatting that is urgent. the files must be in high definition for the printer. For a trade show we need to see the pdf file with slogans and photos. I expect from you a nice and attractive formatting that is urgent. the files must be in high definition for the printer. For a trade show we need to see the pdf file with slogans and photos. I expect from you a nice and attractive formatting that is urgent. the files must be in high definition for the printer. For a trade show we need to see the pdf file with slogans and photos. I expect from you a nice and attractive formatting that is urgent. the files must be in high definition for the printer. For a trade show we need to see the pdf file with slogans and photos. I expect from you a nice and attractive formatting that is urgent. the files must be in high definition for the printer.

Target Market(s)

Professional

Industry/Entity Type

Trade

Requirements
Must have
• the project the messages and the photos are chosen all the way to a nice and professional result. This is urgently the size of the rollup is 200/85.
Nice to have
• the bottom of the rollup on 40 cm must be just color because in an exhibition the visitors can not see the messages near the ground.
Should not have
• no green color

```html
<!DOCTYPE html>
<html lang="fr">
<head>
<meta charset="utf-8">
<title>Nestora – roll-ups salon</title>
<link rel="stylesheet" href="https://fonts.googleapis.com/css2?family=Montserrat+Alternates:wght@500;600&display=swap">
<style>
  :root {
    --page-bg: #ececec;
    --brand-blue: #1d6fcb;
    --brand-grey: #6a6a6a;
    --text-light: #ffffff;
    --font-main: "Montserrat Alternates", "Helvetica Neue", Arial, sans-serif;
  }
  * { margin: 0; padding: 0; box-sizing: border-box; }
  html, body {
    width: 1200px;
    height: 900px;
    overflow: hidden;
    background: var(--page-bg);
    font-family: var(--font-main);
  }
  .rollup-row {
    display: flex;
    justify-content: center;
    gap: 50px;
    padding-top: 50px;
  }
  .rollup {
    position: relative;
    width: 340px;
    height: 800px;
    color: var(--text-light);
    text-align: center;
    box-shadow: 0 6px 18px rgba(0,0,0,0.18);
  }
  .rollup--blue { background: var(--brand-blue); }
  .rollup--grey { background: var(--brand-grey); }

  .brand {
    position: absolute;
    top: 128px;
    left: 0;
    right: 0;
    display: flex;
    justify-content: center;
    align-items: center;
    gap: 12px;
    font-weight: 500;
    font-size: 36px;
    letter-spacing: -0.5px;
    color: var(--text-light);
  }
  .brand__dot {
    width: 26px;
    height: 26px;
    border-radius: 50%;
    background: var(--text-light);
  }
  .headline {
    position: absolute;
    top: 212px;
    left: 18px;
    right: 18px;
    font-size: 15px;
    font-weight: 600;
    line-height: 1.45;
  }
  .photo {
    position: absolute;
    top: 290px;
    left: 0;
    width: 100%;
    height: 225px;
  }
  .photo--surprised {
    background: linear-gradient(120deg, #e9ecef 0%, #c9d3de 35%, #7d93ad 60%, #e2e4e6 100%);
  }
  .photo--fortune {
    background: radial-gradient(circle at 50% 62%, #fff6e0 0%, #e0a95a 14%, #6b3f1d 38%, #2a170c 75%);
  }
  .photo--paperwork {
    background: linear-gradient(90deg, #c9484c 0%, #eceae6 22%, #f5f3f0 50%, #e6e3df 78%, #4fb0b8 100%);
  }
  .tagline {
    position: absolute;
    top: 552px;
    left: 18px;
    right: 18px;
    font-size: 15px;
    font-weight: 600;
    line-height: 1.45;
  }
</style>
</head>
<body>
  <main class="rollup-row">
    <section class="rollup rollup--blue">
      <div class="brand"><span class="brand__dot"></span>nestora.com</div>
      <p class="headline">La réalisation d'un DTG<br>va étonner plus d'un copropriétaire&nbsp;!!</p>
      <div class="photo photo--surprised" role="img" aria-label="Photo : deux hommes surpris regardant l'objectif"></div>
      <p class="tagline">Le DTG, l'outil qui optimise<br>vos charges et votre patrimoine…</p>
    </section>

    <section class="rollup rollup--grey">
      <div class="brand"><span class="brand__dot"></span>nestora.com</div>
      <p class="headline">Nous ne pourrons pas prédire<br>votre avenir…</p>
      <div class="photo photo--fortune" role="img" aria-label="Photo : voyante devant une boule de cristal lumineuse et des bougies"></div>
      <p class="tagline">mais avec le DTG,<br>celui de votre immeuble<br>pour les 10 prochaines années&nbsp;!!</p>
    </section>

    <section class="rollup rollup--grey">
      <div class="brand"><span class="brand__dot"></span>nestora.com</div>
      <p class="headline">Finis le stress pour la gestion<br>de vos copropriétés…</p>
      <div class="photo photo--paperwork" role="img" aria-label="Photo : femme débordée entourée de classeurs et de dossiers"></div>
      <p class="tagline">NESTORA le portail dédié<br>aux professionnels de l'immobilier</p>
    </section>
  </main>
</body>
</html>
```